Landing page for 'Page under construction' page

We need a simple landing page that we can use while our page is under construction.

The page should be made ready so that all we need to do is drop it on our web server and then it will function as our webpage. The domain is www.tlv.no

Please see attached file for instructions on what elements to include in the landing page. The Brand Book provides fonts and color palette.

Coding

Coded - Design and coding required

Number of Pages Required

1 page

Colors

Designer to choose colors to be used in the design.

```html
<!DOCTYPE html>
<html lang="en">
<head>
<meta charset="utf-8">
<title>Talvik – Page is under Construction</title>
<link rel="stylesheet" href="https://fonts.googleapis.com/css2?family=Montserrat:wght@400;500;600;700&family=Nunito+Sans:wght@400;600&display=swap">
<style>
:root{
  --navy:#0a3268;
  --navy-deep:#08305f;
  --orange:#f0883e;
  --coral:#e9584e;
  --blush:#fcefee;
  --cream:#fef6ef;
  --white:#ffffff;
}
*{box-sizing:border-box;margin:0;padding:0}
html,body{width:1200px;height:2947px;overflow:hidden;background:var(--white)}
body{position:relative;font-family:"Montserrat",sans-serif;color:var(--navy)}
.abs{position:absolute}
.hero{left:0;top:0;width:1200px;height:673px;
  background:linear-gradient(120deg,#3ea4b0 0%,#2f7fa3 45%,#245a8d 80%,#2a4f86 100%)}
.brand{left:0;top:52px;width:1200px;text-align:center;color:var(--white);
  font-weight:700;font-size:50px;letter-spacing:1px}
.hero-title{left:0;top:258px;width:1200px;text-align:center;color:var(--white);
  font-weight:700;font-size:66px;line-height:76px}
.blush-block{left:0;top:673px;width:164px;height:350px;background:var(--blush)}
.cream-block{left:816px;top:1023px;width:384px;height:534px;background:var(--cream)}
.eyebrow{left:0;top:781px;width:1200px;text-align:center;font-size:13px;font-weight:600;
  color:var(--orange);letter-spacing:1px}
.about-heading{left:0;top:818px;width:1200px;text-align:center;font-weight:500;
  font-size:26px;line-height:31px;letter-spacing:3.3px;color:var(--navy)}
.accent-bar{height:4px;width:88px;border-radius:2px;
  background:linear-gradient(90deg,var(--orange),var(--coral))}
.about-bar{left:556px;top:902px}
.about-text{left:280px;top:1128px;width:285px;font-size:15.3px;line-height:22px;
  letter-spacing:1.6px;color:var(--navy)}
.photo{border-radius:3px}
.photo-desk{left:681px;top:1074px;width:358px;height:432px;
  background:linear-gradient(160deg,#a9cbc7 0%,#d9dfdc 45%,#8a8f92 100%)}
.photo-bulb{left:165px;top:1677px;width:428px;height:419px;
  background:linear-gradient(180deg,#bcd6d8 0%,#e6c6c4 55%,#f8958e 100%)}
.photo-eagle{left:607px;top:2097px;width:428px;height:418px;
  background:linear-gradient(120deg,#f8f2ee 0%,#efe6df 45%,#4a3129 75%,#2c211d 100%)}
.card{background:var(--navy);color:var(--white);border-radius:4px;
  box-shadow:0 14px 30px rgba(10,50,104,.18);padding:40px 30px}
.card-vision{left:593px;top:1757px;width:442px;height:260px}
.card-focus{left:165px;top:2178px;width:442px;height:254px;padding-left:27px}
.card h2{font-weight:500;font-size:25px;line-height:30px}
.card .accent-bar{margin:14px 0 24px}
.card p{font-family:"Nunito Sans",sans-serif;font-weight:600;font-size:15.6px;line-height:26.5px}
.newsletter{left:53px;top:2593px;width:1094px;height:306px;background:var(--navy-deep);
  border-radius:6px;color:var(--white);text-align:center;box-shadow:0 14px 30px rgba(10,50,104,.2)}
.nl-eyebrow{position:absolute;left:0;top:40px;width:100%;font-size:13px;font-weight:700;letter-spacing:1.5px}
.nl-heading{position:absolute;left:0;top:80px;width:100%;font-size:27px;font-weight:500;letter-spacing:4.3px}
.nl-field{position:absolute;left:395px;top:138px;width:302px;height:37px;background:var(--white);border-radius:19px}
.nl-send{position:absolute;right:3px;top:3px;width:31px;height:31px}
.nl-mail-label{position:absolute;left:0;top:210px;width:100%;font-family:"Nunito Sans",sans-serif;font-weight:600;font-size:15px}
.nl-mail{position:absolute;left:0;top:236px;width:100%;font-size:19px;font-weight:500;letter-spacing:.5px}
</style>
</head>
<body>
<section class="abs hero" role="img" aria-label="Photo looking up between tall office towers, tinted teal and blue"></section>
<div class="abs brand">Talvik</div>
<h1 class="abs hero-title">Page is under<br>Construction</h1>

<div class="abs blush-block"></div>
<div class="abs cream-block"></div>

<p class="abs eyebrow">About Us</p>
<h2 class="abs about-heading">Digital solutions and data-driven<br>business development that create value</h2>
<div class="abs accent-bar about-bar"></div>

<p class="abs about-text">TLV Consulting is a consulting company with cutting-edge expertise in digitalisation and data-driven business development. We have extensive experience in data warehouse development, data analysis and reporting, EPM and planning solutions, budget and forecasting solutions for financial and financial data. In short, we help our customers exploit the potential in the available data.</p>
<div class="abs photo photo-desk" role="img" aria-label="Photo of hands writing notes on paper beside two laptops"></div>

<div class="abs photo photo-bulb" role="img" aria-label="Photo of a hand holding a light bulb against a pastel sky"></div>
<article class="abs card card-vision">
  <h2>TLV Vision</h2>
  <div class="accent-bar"></div>
  <p>TLV will be the country's leading supplier and competence house on Talvik software and digital solutions for business management.</p>
</article>

<article class="abs card card-focus">
  <h2>Focus</h2>
  <div class="accent-bar"></div>
  <p>TLV will be the country's leading supplier and competence house on Talvik software and digital solutions for business management.</p>
</article>
<div class="abs photo photo-eagle" role="img" aria-label="Photo of a bird of prey in profile on a pale background"></div>

<section class="abs newsletter">
  <p class="nl-eyebrow">Get in touch</p>
  <h2 class="nl-heading">Subscribe to our newsletter to stay updated</h2>
  <div class="nl-field">
    <svg class="nl-send" viewBox="0 0 31 31" aria-hidden="true">
      <defs><linearGradient id="sendGrad" x1="0" y1="0" x2="1" y2="1"><stop offset="0" stop-color="#f0883e"/><stop offset="1" stop-color="#e9584e"/></linearGradient></defs>
      <circle cx="15.5" cy="15.5" r="15.5" fill="url(#sendGrad)"/>
      <path d="M9 16 L22 10 L17 22 L15.5 17 Z" fill="#fff"/>
    </svg>
  </div>
  <p class="nl-mail-label">or mail us at</p>
  <p class="nl-mail">media@tlv.no</p>
</section>
</body>
</html>
```